Healthcare IT company looking for business card design

We develop IT systems for healthcare that significantly reduces cost and improves quality.

We want a business card design that is professional and clean, and using the colors in our logo.

Doctors and decision makers in the healthcare industry

Healthcare

It should include
Name and title, address, telephone

Torvald Eskberg, CEO
+46 712 480517
torvald@velpamo.se

Serif

0355a3
ed282f

• Clean design
• Professional feel
• N/A
• N/A

```html
<!DOCTYPE html>
<html lang="en">
<head>
<meta charset="utf-8">
<title>Velpamo Business Card</title>
<link rel="stylesheet" href="https://fonts.googleapis.com/css2?family=Source+Sans+3:wght@400;600&display=swap">
<style>
  :root {
    --backdrop: #d9d6d2;
    --card: #121212;
    --brand-blue: #1a66c2;
    --brand-red: #ed282f;
    --ink-light: #e8e8e8;
    --ink-soft: #b9b9b9;
    --rule: #cfcfcf;
  }
  * { margin: 0; padding: 0; box-sizing: border-box; }
  html, body { width: 1200px; height: 814px; overflow: hidden; }
  body {
    background: var(--backdrop);
    font-family: "Source Sans 3", "Myriad Pro", Arial, sans-serif;
    position: relative;
  }
  .card {
    position: absolute;
    top: 257px;
    width: 525px;
    height: 300px;
    background: var(--card);
    border-radius: 3px;
    box-shadow: 0 6px 18px rgba(0,0,0,0.25);
  }
  .card-front { left: 60px; }
  .card-back { left: 615px; }

  .brand-name {
    position: absolute;
    top: 40px;
    right: 40px;
    color: var(--brand-blue);
    font-weight: 600;
    font-size: 44px;
    line-height: 1;
    letter-spacing: 0.5px;
  }
  .brand-dot {
    position: absolute;
    top: 30px;
    right: 40px;
    width: 10px;
    height: 10px;
    border-radius: 50%;
    background: var(--brand-red);
  }
  .divider {
    position: absolute;
    top: 140px;
    left: 40px;
    right: 40px;
    height: 1px;
    background: var(--rule);
  }
  .address {
    position: absolute;
    top: 158px;
    right: 40px;
    text-align: right;
    color: var(--ink-light);
    font-size: 14px;
    line-height: 1.35;
  }
  .person {
    position: absolute;
    left: 40px;
    top: 186px;
  }
  .person-name {
    color: var(--brand-blue);
    font-weight: 600;
    font-size: 19px;
    line-height: 1.1;
  }
  .person-title {
    color: var(--brand-red);
    font-size: 14px;
    margin-top: 2px;
  }
  .contact-list { list-style: none; margin-top: 4px; }
  .contact-list li {
    display: flex;
    align-items: center;
    gap: 8px;
    color: var(--ink-light);
    font-size: 15px;
    line-height: 20px;
  }
  .contact-icon { width: 12px; height: 12px; fill: var(--brand-blue); flex: none; }

  .back-brand {
    position: absolute;
    top: 110px;
    left: 0;
    right: 0;
    text-align: center;
    color: var(--ink-soft);
    font-weight: 600;
    font-size: 48px;
    line-height: 1;
  }
  .back-web {
    position: absolute;
    top: 200px;
    left: 0;
    right: 0;
    text-align: center;
    color: var(--ink-light);
    font-size: 12px;
    letter-spacing: 5px;
  }
</style>
</head>
<body>
  <section class="card card-front">
    <span class="brand-dot"></span>
    <div class="brand-name">Velpamo</div>
    <div class="divider"></div>
    <address class="address">4120 Larkspur Road<br>Fairbanks, Alaska 99712</address>
    <div class="person">
      <div class="person-name">Torvald Eskberg</div>
      <div class="person-title">CEO</div>
      <ul class="contact-list">
        <li>
          <svg class="contact-icon" viewBox="0 0 24 24"><path d="M6.6 10.8a15.2 15.2 0 0 0 6.6 6.6l2.2-2.2c.3-.3.7-.4 1-.2 1.1.4 2.3.6 3.6.6.6 0 1 .4 1 1V20c0 .6-.4 1-1 1A17 17 0 0 1 3 4c0-.6.4-1 1-1h3.5c.6 0 1 .4 1 1 0 1.3.2 2.5.6 3.6.1.3 0 .7-.2 1z"/></svg>
          +46 712 480517
        </li>
        <li>
          <svg class="contact-icon" viewBox="0 0 24 24"><path d="M2 5h20v14H2z M2 5l10 8 10-8" fill="none" stroke="#1a66c2" stroke-width="2.5"/></svg>
          torvald@velpamo.se
        </li>
        <li>
          <svg class="contact-icon" viewBox="0 0 24 24"><circle cx="12" cy="12" r="10" fill="none" stroke="#1a66c2" stroke-width="2.5"/><path d="M2 12h20M12 2c3 3 3 17 0 20M12 2c-3 3-3 17 0 20" fill="none" stroke="#1a66c2" stroke-width="2"/></svg>
          www.velpamo.se
        </li>
      </ul>
    </div>
  </section>

  <section class="card card-back">
    <div class="back-brand">Velpamo</div>
    <div class="back-web">www.velpamo.se</div>
  </section>
</body>
</html>
```